Rural contractor needs professional informative business card

We need a business card design that looks professional but also includes information about the services that the business offers.
The business is an earthmoving and transport business. All of the services offered are listed on the old card attached.
The business is aimed at farmers so the design we are after is a classic look. The card needs to include all of the information that is listed on the old card design uploaded as an attachment. We recognize that this is a lot of information to fit on a business card but it also operates as a key marketing tool so is very important to the business.
Feel free to send me your questions.
Thanks
Reason: We are having trouble deciding between all these great designs - thank you for your efforts
We would love to see some designs using red with a little white and black. Also feel free to re-design our logo if you feel it needs to be to fit your designs. Thank you

```html
<!DOCTYPE html>
<html lang="en">
<head>
<meta charset="utf-8">
<title>Harlow Contracting – Business Card</title>
<link href="https://fonts.googleapis.com/css2?family=Open+Sans:wght@400;600&display=swap" rel="stylesheet">
<style>
  :root{
    --red:#e3222b;
    --red-deep:#b5121b;
    --black:#141414;
    --white:#ffffff;
    --paper:#f1f1f1;
    --stage:#e9e6e1;
    --photo-dark:#2a2a2a;
    --photo-sky:#9aa7b3;
    --photo-yellow:#e2b21c;
  }
  *{box-sizing:border-box;margin:0;padding:0}
  html,body{width:704px;height:1200px;overflow:hidden}
  body{
    background:var(--stage);
    font-family:"Open Sans",Arial,sans-serif;
    position:relative;
  }
  .card{
    position:absolute;left:72px;width:560px;height:320px;
    border-radius:18px;overflow:hidden;
    background:linear-gradient(160deg,var(--red) 0%,var(--red) 60%,var(--red-deep) 100%);
    box-shadow:0 6px 18px rgba(0,0,0,.18);
    color:var(--white);
  }
  .card--front{top:110px}
  .card--back{top:700px}

  /* shared */
  .wordmark{font-weight:400;line-height:1.05;letter-spacing:.5px}
  .wordmark__rule{display:block;height:2px;margin-top:6px}
  .service-list{list-style:none;font-size:13px;line-height:1.35}
  .service-list li{position:relative;padding-left:20px}
  .service-list li::before{
    content:"";position:absolute;left:3px;top:3px;width:5px;height:9px;
    border-right:2px solid currentColor;border-bottom:2px solid currentColor;
    transform:rotate(40deg);
  }
  .service-heading{font-size:14px;margin-bottom:2px}

  /* front */
  .front__wordmark{position:absolute;left:34px;top:30px;font-size:30px;color:var(--white)}
  .front__wordmark .wordmark__rule{background:var(--white);width:250px}
  .front__transport{position:absolute;left:36px;top:100px}
  .front__earthmoving{position:absolute;left:318px;top:30px}
  .front__stripe{
    position:absolute;right:32px;top:0;bottom:0;width:22px;background:var(--black);
    border-left:3px solid var(--white);
  }
  .front__photo{
    position:absolute;left:0;right:0;bottom:0;height:104px;
    background:linear-gradient(180deg,var(--photo-sky) 0%,#5c6268 45%,var(--photo-dark) 100%);
  }

  /* back */
  .back__monogram{
    position:absolute;left:70px;top:34px;width:84px;height:84px;
    border:2px solid rgba(255,255,255,.85);border-radius:50%;
  }
  .back__contact{position:absolute;left:34px;top:168px;font-size:13px;line-height:1.55}
  .back__name{font-size:14px;margin-bottom:4px}
  .contact-row{display:flex;align-items:center;gap:8px}
  .contact-row svg{width:12px;height:12px;flex:none;fill:var(--white)}
  .back__band{
    position:absolute;left:286px;top:0;bottom:0;width:30px;background:var(--black);
    border-left:3px solid var(--white);
  }
  .back__tagline{
    position:absolute;left:301px;top:50%;white-space:nowrap;
    transform:translate(-50%,-50%) rotate(-90deg);
    font-size:11px;letter-spacing:.8px;color:var(--white);
  }
  .back__panel{
    position:absolute;left:316px;top:0;right:0;bottom:0;background:var(--paper);
    color:var(--black);
  }
  .back__photo{
    position:absolute;left:26px;right:22px;top:26px;height:150px;border-radius:6px;
    background:radial-gradient(ellipse at 60% 45%,var(--photo-yellow) 0%,#c48f12 40%,var(--paper) 75%);
  }
  .back__wordmark{position:absolute;left:24px;bottom:40px;font-size:26px;color:var(--black)}
  .back__wordmark .wordmark__rule{background:var(--black);width:190px}
</style>
</head>
<body>

<section class="card card--front" aria-label="Business card front">
  <div class="front__photo" role="img" aria-label="Photo of a prime mover truck, loader and earthmoving plant on site"></div>
  <div class="front__stripe"></div>

  <div class="wordmark front__wordmark">Harlow Contracting<span class="wordmark__rule"></span></div>

  <div class="front__transport">
    <p class="service-heading">Transport</p>
    <ul class="service-list">
      <li>Road building &amp; maintenance</li>
      <li>Poly pipe laying</li>
      <li>Clearing fence lines</li>
      <li>Sand &amp; gravel supplies</li>
    </ul>
  </div>

  <div class="front__earthmoving">
    <p class="service-heading">Earthmoving</p>
    <ul class="service-list">
      <li>Grain</li>
      <li>Cotton</li>
      <li>Wool</li>
      <li>Sand &amp; gravel</li>
    </ul>
  </div>
</section>

<section class="card card--back" aria-label="Business card back">
  <div class="back__monogram"></div>

  <div class="back__contact">
    <p class="back__name">Rhys Harlow</p>
    <p class="contact-row">
      <svg viewBox="0 0 24 24" aria-hidden="true"><path d="M6.6 10.8a15.1 15.1 0 0 0 6.6 6.6l2.2-2.2a1 1 0 0 1 1-.25 11.4 11.4 0 0 0 3.6.57 1 1 0 0 1 1 1V20a1 1 0 0 1-1 1A17 17 0 0 1 3 4a1 1 0 0 1 1-1h3.5a1 1 0 0 1 1 1c0 1.25.2 2.45.57 3.57a1 1 0 0 1-.25 1z"/></svg>
      0491 570 156
    </p>
    <p class="contact-row">
      <svg viewBox="0 0 24 24" aria-hidden="true"><path d="M12 2a7 7 0 0 0-7 7c0 5.25 7 13 7 13s7-7.75 7-13a7 7 0 0 0-7-7zm0 9.5A2.5 2.5 0 1 1 12 6.5a2.5 2.5 0 0 1 0 5z"/></svg>
      42 Wattle Street, Dunmore 2899
    </p>
    <p class="contact-row">
      <svg viewBox="0 0 24 24" aria-hidden="true"><path d="M2 5h20v14H2zm2 2v.5l8 5 8-5V7l-8 5z"/></svg>
      rhys@harlowcontracting.com
    </p>
  </div>

  <div class="back__band"></div>
  <p class="back__tagline">EARTHMOVING &amp; TRANSPORT SOLUTIONS</p>

  <div class="back__panel">
    <div class="back__photo" role="img" aria-label="Photo of a yellow front-end loader"></div>
    <div class="wordmark back__wordmark">Harlow Contracting<span class="wordmark__rule"></span></div>
  </div>
</section>

</body>
</html>
```